Looking for updated Letterhead and Compliments Slips to go with our new updated logo. This stationary will be used for letters to suppliers and customers so needs to be practical while also quite classic.

We are an engineering company so needs to be clean and precise

Target Market(s)

SME'S and large automotive customers

Industry/Entity Type

Automotive

Font styles to use
Sans Serif

Colors
85acd3
0356a4
0792cd
33a6d7
85abd2
ffffff

Requirements
Must have
• Address details as below
• KT Fabrications Limited
• Hallmere Road
• Rugby
• Warwickshire
• LP47 9XZ, UK
• Telephone: +44 (0)1632 960418
• Fax: +44 (0)1632 960733
• Email: sales@ktfabrications.example
• Web: www.ktfabrications.example
Nice to have
• Nice to have some element of being a British Manufacturer

```html
<!DOCTYPE html>
<html lang="en">
<head>
<meta charset="utf-8">
<title>KT Fabrications – Letterhead and Compliments Slip</title>
<link rel="stylesheet" href="https://fonts.googleapis.com/css2?family=Source+Sans+3:wght@400;600&family=Great+Vibes&display=swap">
<style>
  :root {
    --brand-blue: #0356a4;
    --sky-blue: #85acd3;
    --ink: #2a2a2a;
    --band-dark: #1e1e1e;
    --paper: #ffffff;
    --paper-shade: #f1f2f4;
    --canvas: #e4e4e4;
    --faint: #e9ebef;
  }
  * { box-sizing: border-box; margin: 0; padding: 0; }
  html, body { width: 1200px; height: 1112px; overflow: hidden; }
  body {
    background: var(--canvas);
    font-family: "Source Sans 3", "Myriad Pro", Arial, sans-serif;
    color: var(--ink);
    position: relative;
  }
  .sheet-label {
    position: absolute; top: 18px; width: 562px; text-align: center;
    font-weight: 600; font-size: 30px; color: #555;
  }
  .sheet {
    position: absolute;
    background: linear-gradient(160deg, var(--paper) 0%, var(--paper) 45%, var(--paper-shade) 100%);
    box-shadow: 0 2px 6px rgba(0,0,0,.18);
    overflow: hidden;
  }
  .letterhead { width: 562px; height: 726px; top: 58px; }
  .letterhead--filled { left: 17px; }
  .letterhead--blank { left: 617px; }
  .compliments { width: 546px; height: 257px; left: 321px; top: 831px; }

  .brand-name {
    position: absolute; left: 24px; top: 80px;
    font-size: 17px; font-weight: 600; letter-spacing: 5px;
    color: var(--brand-blue); white-space: nowrap;
    display: flex; align-items: center; gap: 8px;
  }
  .brand-dot { width: 12px; height: 12px; border-radius: 50%; background: var(--brand-blue); display: inline-block; }

  .contact {
    position: absolute; right: 16px; top: 38px;
    border-left: 1px solid #c9ccd2; padding-left: 13px;
    font-size: 10.5px; line-height: 17.5px; color: #3a3a3a;
  }
  .compliments .contact { right: 12px; }
  .contact li { list-style: none; display: flex; align-items: center; gap: 5px; white-space: nowrap; }
  .icon { width: 9px; height: 9px; fill: var(--brand-blue); flex: none; }

  .letter { position: absolute; left: 24px; top: 140px; width: 512px; font-size: 11px; line-height: 16.4px; }
  .letter .date { margin-bottom: 4px; }
  .letter .recipient { line-height: 13px; margin-bottom: 19px; }
  .letter .salutation { margin-bottom: 11px; }
  .letter p.body { margin-bottom: 19px; }
  .letter .closing { margin-top: 36px; }
  .signature { font-family: "Great Vibes", cursive; color: var(--brand-blue); font-size: 22px; line-height: 26px; }

  .watermark {
    position: absolute; border-radius: 50%; background: var(--faint); opacity: .7;
  }
  .letterhead--filled .watermark { width: 150px; height: 150px; left: 410px; top: 520px; }
  .letterhead--blank .watermark { width: 320px; height: 320px; left: 121px; top: 270px; }

  .address { position: absolute; left: 24px; top: 681px; font-size: 10.5px; line-height: 14px; }
  .compliments .address { left: 14px; top: 212px; }
  .address .company { color: var(--brand-blue); display: flex; align-items: center; gap: 4px; }
  .address .street { padding-left: 12px; }

  .footer-bands { position: absolute; left: 0; }
  .letterhead .footer-bands { top: 702px; }
  .compliments .footer-bands { top: 234px; }
  .band-dark { fill: var(--band-dark); }
  .band-blue { fill: var(--brand-blue); }
  .web {
    position: absolute; color: #fff; font-size: 12px; letter-spacing: 2.2px; white-space: nowrap;
  }
  .letterhead .web { right: 14px; top: 705px; }
  .compliments .web { right: 12px; top: 237px; }
  .compliments-line {
    position: absolute; right: 12px; top: 186px;
    font-family: "Great Vibes", cursive; font-size: 33px; color: #333;
  }
</style>
</head>
<body>

<svg width="0" height="0" style="position:absolute" aria-hidden="true">
  <defs>
    <symbol id="i-phone" viewBox="0 0 10 10"><path d="M2 0.5l2 2-1 1.2c.6 1.3 1.6 2.3 2.9 2.9l1.2-1 2 2-1.3 1.8C4.6 9.2.8 5.4.4 1.9z"/></symbol>
    <symbol id="i-fax" viewBox="0 0 10 10"><path d="M2.5 0.5h5v3h-5zM0.5 4h9v4h-1.5v1.5h-6V8H0.5z"/></symbol>
    <symbol id="i-mail" viewBox="0 0 10 10"><path d="M0.5 2h9v6.5h-9zM1.3 2.8L5 5.6l3.7-2.8z" fill-rule="evenodd"/></symbol>
    <symbol id="i-pin" viewBox="0 0 10 10"><path d="M5 0.3a3.6 3.6 0 0 1 3.6 3.6C8.6 6.6 5 9.7 5 9.7S1.4 6.6 1.4 3.9A3.6 3.6 0 0 1 5 .3zm0 2.2a1.4 1.4 0 1 0 0 2.8 1.4 1.4 0 0 0 0-2.8z" fill-rule="evenodd"/></symbol>
  </defs>
</svg>

<div class="sheet-label" style="left:17px">LH_1</div>
<div class="sheet-label" style="left:617px">LH_2</div>

<!-- Letterhead with sample letter -->
<section class="sheet letterhead letterhead--filled">
  <div class="watermark" aria-hidden="true"></div>
  <div class="brand-name"><span class="brand-dot"></span>KT FABRICATIONS</div>
  <ul class="contact">
    <li><svg class="icon"><use href="#i-phone"/></svg>+44 (0)1632 960418</li>
    <li><svg class="icon"><use href="#i-fax"/></svg>+44 (0)1632 960733</li>
    <li><svg class="icon"><use href="#i-mail"/></svg>sales@ktfabrications.example</li>
  </ul>
  <div class="letter">
    <p class="date">May 05, 2017</p>
    <p class="recipient">Your Name<br>Title</p>
    <p class="salutation">Dear Mr. Lorem,</p>
    <p class="body">Lorem ipsum dolor sit amet, consectetuer adipiscing elit, sed diam nonummy nibh euismod tincidunt ut laoreet dolore magna aliquam erat volutpat. Ut wisi enim ad minim veniam, quis nostrud exerci tation ullamcorper suscipit lobortis nisl ut aliquip ex ea commodo consequat. Duis autem vel eum iriure dolor in hendrerit in vulputate velit esse molestie consequat, vel illum dolore eu feugiat nulla facilisis at vero eros et accumsan et iusto odio dignissim qui blandit praesent luptatum zzril delenit augue duis dolore te feugait nulla facilisi.</p>
    <p class="body">Lorem ipsum dolor sit amet, consectetuer adipiscing elit, sed diam nonummy nibh euismod tincidunt ut laoreet dolore magna aliquam erat volutpat. Ut wisi enim ad minim veniam, quis nostrud exerci tation ullamcorper suscipit lobortis nisl ut aliquip ex ea commodo consequat. Duis autem vel eum iriure dolor in hendrerit in vulputate velit esse molestie consequat, vel illum dolore eu feugiat nulla facilisis at vero eros et accumsan et iusto odio dignissim qui blandit praesent luptatum zzril delenit augue duis dolore te feugait nulla facilisi.</p>
    <p class="body">Lorem ipsum dolor sit amet, consectetuer adipiscing elit, sed diam nonummy nibh euismod tincidunt ut laoreet dolore magna aliquam erat volutpat. Ut wisi enim ad minim veniam, quis nostrud exerci tation ullamcorper suscipit lobortis nisl ut aliquip ex ea commodo consequat. Duis autem vel eum iriure dolor in hendrerit in vulputate velit esse molestie consequat, vel illum dolore eu feugiat nulla facilisis at vero eros et accumsan et iusto odio dignissim qui blandit praesent luptatum zzril delenit augue duis dolore te feugait nulla facilisi.</p>
    <p class="closing">Sincerely Your,</p>
    <p class="signature">Your Name</p>
  </div>
  <div class="address">
    <p class="company"><svg class="icon"><use href="#i-pin"/></svg>KT Fabrications Limited</p>
    <p class="street">Hallmere Road, Rugby, Warwickshire, LP47 9XZ, UK</p>
  </div>
  <svg class="footer-bands" width="562" height="24" aria-hidden="true">
    <polygon class="band-dark" points="0,12 305,12 293,24 0,24"/>
    <polygon class="band-blue" points="302,24 326,0 562,0 562,24"/>
  </svg>
  <p class="web">www.ktfabrications.example</p>
</section>

<!-- Blank letterhead -->
<section class="sheet letterhead letterhead--blank">
  <div class="watermark" aria-hidden="true"></div>
  <div class="brand-name"><span class="brand-dot"></span>KT FABRICATIONS</div>
  <ul class="contact">
    <li><svg class="icon"><use href="#i-phone"/></svg>+44 (0)1632 960418</li>
    <li><svg class="icon"><use href="#i-fax"/></svg>+44 (0)1632 960733</li>
    <li><svg class="icon"><use href="#i-mail"/></svg>sales@ktfabrications.example</li>
  </ul>
  <div class="address">
    <p class="company"><svg class="icon"><use href="#i-pin"/></svg>KT Fabrications Limited</p>
    <p class="street">Hallmere Road, Rugby, Warwickshire, LP47 9XZ, UK</p>
  </div>
  <svg class="footer-bands" width="562" height="24" aria-hidden="true">
    <polygon class="band-dark" points="0,12 305,12 293,24 0,24"/>
    <polygon class="band-blue" points="302,24 326,0 562,0 562,24"/>
  </svg>
  <p class="web">www.ktfabrications.example</p>
</section>

<!-- Compliments slip -->
<section class="sheet compliments">
  <div class="brand-name" style="top:80px; left:14px"><span class="brand-dot"></span>KT FABRICATIONS</div>
  <ul class="contact">
    <li><svg class="icon"><use href="#i-phone"/></svg>+44 (0)1632 960418</li>
    <li><svg class="icon"><use href="#i-fax"/></svg>+44 (0)1632 960733</li>
    <li><svg class="icon"><use href="#i-mail"/></svg>sales@ktfabrications.example</li>
  </ul>
  <p class="compliments-line">With compliments</p>
  <div class="address">
    <p class="company"><svg class="icon"><use href="#i-pin"/></svg>KT Fabrications Limited</p>
    <p class="street">Hallmere Road, Rugby, Warwickshire, LP47 9XZ, UK</p>
  </div>
  <svg class="footer-bands" width="546" height="23" aria-hidden="true">
    <polygon class="band-dark" points="0,12 290,12 279,23 0,23"/>
    <polygon class="band-blue" points="288,23 311,0 546,0 546,23"/>
  </svg>
  <p class="web">www.ktfabrications.example</p>
</section>

</body>
</html>
```